Automotive Accessories Business Card

Design a business template that match our new logo design and our industry.

https://www.kelvorauto.com/

Target Market(s)

Aftermarket auto parts and accessories

Industry/Entity Type

automotive

Contact Information for Business Card

company logo

Font styles to use
Serif
Sans Serif

Colors
EB3D1F
EC4F4E
F09395
F8D3D4
FCEDEE

```html
<!DOCTYPE html>
<html lang="en">
<head>
<meta charset="utf-8">
<title>Kelvor Auto Parts – Business Card</title>
<link href="https://fonts.googleapis.com/css2?family=Arimo:wght@400;700&display=swap" rel="stylesheet">
<style>
  :root {
    --stage: #2a2a2a;
    --card: #0d0d0d;
    --red: #e0232b;
    --white: #ffffff;
    --silver: #c9c9c9;
    --divider: #555555;
  }
  * { margin: 0; padding: 0; box-sizing: border-box; }
  html, body { width: 1200px; height: 900px; overflow: hidden; }
  body {
    background: var(--stage);
    font-family: "Arimo", Arial, sans-serif;
    display: flex;
    align-items: center;
    justify-content: center;
    gap: 60px;
  }
  .card {
    width: 520px;
    height: 297px;
    background: var(--card);
    border-radius: 22px;
    position: relative;
  }
  .card-front { display: flex; align-items: center; padding: 0 34px; }
  .brand {
    display: flex;
    align-items: center;
    gap: 10px;
    width: 205px;
  }
  .brand-mark { width: 16px; height: 16px; background: var(--red); flex: none; }
  .brand-name {
    font-weight: 700;
    font-size: 19px;
    line-height: 1.15;
    letter-spacing: 0.5px;
    color: var(--red);
  }
  .divider { width: 1px; height: 170px; background: var(--divider); margin: 0 24px 0 10px; }
  .contact { color: var(--white); }
  .person-name {
    font-weight: 700;
    font-size: 19px;
    letter-spacing: 0.5px;
    color: var(--red);
    text-transform: uppercase;
  }
  .person-role { font-size: 14px; margin-bottom: 12px; }
  .contact-list { list-style: none; font-size: 13.5px; line-height: 1.5; }
  .contact-list li { display: flex; align-items: center; gap: 7px; }
  .contact-list svg { width: 13px; height: 13px; flex: none; }
  .accent { color: var(--red); }
  .address { font-size: 13.5px; line-height: 1.35; margin-top: 10px; }
  .card-back { display: flex; align-items: center; justify-content: center; }
  .card-back .brand { width: auto; }
  .card-back .brand-mark { background: var(--silver); width: 20px; height: 20px; }
  .card-back .brand-name { color: var(--silver); font-size: 28px; }
</style>
</head>
<body>
  <section class="card card-front">
    <div class="brand">
      <span class="brand-mark"></span>
      <span class="brand-name">KELVOR AUTO PARTS</span>
    </div>
    <div class="divider"></div>
    <div class="contact">
      <p class="person-name">Marcus Hale</p>
      <p class="person-role">Managing Director</p>
      <ul class="contact-list">
        <li>
          <svg viewBox="0 0 16 16" aria-hidden="true"><path fill="var(--red)" d="M3.5 1.5l2.5 0 1 3.5-1.8 1.2a9 9 0 0 0 4.6 4.6L11 9l3.5 1v2.5a2 2 0 0 1-2 2A11 11 0 0 1 1.5 3.5a2 2 0 0 1 2-2z"/></svg>
          044-555 018 274
        </li>
        <li>
          <svg viewBox="0 0 16 16" aria-hidden="true"><rect x="1" y="3" width="14" height="10" fill="var(--red)"/><path d="M1 3l7 6 7-6" fill="none" stroke="var(--card)" stroke-width="1.3"/></svg>
          info@kelvormail.com
        </li>
        <li>
          <svg viewBox="0 0 16 16" aria-hidden="true"><g fill="none" stroke="var(--red)" stroke-width="1.4"><circle cx="8" cy="8" r="6.5"/><ellipse cx="8" cy="8" rx="3" ry="6.5"/><path d="M1.5 8h13M2.5 4.8h11M2.5 11.2h11"/></g></svg>
          www.<span class="accent">kelvorauto</span>.com
        </li>
      </ul>
      <p class="address">421, Address line goes here<br>45452,Country Name</p>
    </div>
  </section>

  <section class="card card-back">
    <div class="brand">
      <span class="brand-mark"></span>
      <span class="brand-name">KELVOR AUTO PARTS</span>
    </div>
  </section>
</body>
</html>
```